Boring Fiberglass Repair Company needs creative business cards

The Fiberglass Repair industry isn't very fun or creative but we'd like a business card that communicates a fresh, modern, and service-oriented feel. We repair bathroom fixtures (bath tubs, showers, etc) which are made out of fiberglass. Our fiberglass repair service will be sold to bathtub manufacturers and also businesses that sell bathtubs. We will also offer our services to home owners that have broken showers and bathtubs.
Target Market(s)
Home builders, plumbing wholesalers, home owners
Contact Information for Business Card
Name
Phone Number
Email Address
Business Address
Tag line: "Quality Craftsmanship Today"
Look and feel

```html
<!DOCTYPE html>
<html lang="en">
<head>
<meta charset="UTF-8">
<title>Mesa Ridge Fiberglass – Business Card</title>
<link href="https://fonts.googleapis.com/css2?family=Arimo:wght@400;700&display=swap" rel="stylesheet">
<style>
  :root {
    --bg: #ece9e4;
    --brand-red: #e3202b;
    --brand-red-dark: #b8141e;
    --navy: #223068;
    --navy-light: #34477f;
    --white: #ffffff;
    --rule: rgba(255,255,255,0.55);
  }
  * { margin: 0; padding: 0; box-sizing: border-box; }
  html, body { width: 1200px; height: 900px; overflow: hidden; }
  body {
    background: var(--bg);
    font-family: 'Arimo', Arial, sans-serif;
    position: relative;
  }
  .card {
    position: absolute;
    left: 290px;
    width: 620px;
    height: 354px;
    border-radius: 4px;
    overflow: hidden;
    box-shadow: 0 10px 28px rgba(0,0,0,0.22);
  }
  .card--back {
    top: 72px;
    background: linear-gradient(135deg, #d91822, var(--brand-red) 60%, #e8313a);
    display: flex;
    align-items: center;
    justify-content: center;
  }
  .card--front { top: 470px; background: var(--white); }
  .card__shapes { position: absolute; inset: 0; width: 100%; height: 100%; }

  .wordmark {
    font-weight: 700;
    text-transform: uppercase;
    line-height: 1;
  }
  .wordmark__main { display: block; font-size: 40px; letter-spacing: 1px; }
  .wordmark__sub { display: block; font-size: 17px; letter-spacing: 13px; margin-top: 6px; padding-left: 56px; }
  .card--back .wordmark { color: var(--white); }
  .card--front .wordmark {
    position: absolute; left: 28px; top: 44px; color: var(--navy);
  }

  .person {
    position: absolute;
    right: 340px;
    top: 262px;
    text-align: right;
  }
  .person__role { color: var(--white); font-size: 17px; }
  .person__name { color: var(--brand-red); font-size: 24px; font-weight: 700; text-transform: uppercase; margin-top: 2px; }

  .divider {
    position: absolute; left: 296px; top: 240px;
    width: 1px; height: 92px; background: var(--rule);
  }
  .contact {
    position: absolute; left: 312px; top: 244px; width: 290px;
    list-style: none; color: var(--white); font-size: 14px;
  }
  .contact__item { display: flex; align-items: center; gap: 9px; height: 24px; }
  .contact__item--address { margin-top: 18px; position: relative; }
  .contact__item--address::before {
    content: ""; position: absolute; left: 0; right: 0; top: -10px;
    height: 1px; background: var(--rule);
  }
  .contact__icon { width: 14px; height: 14px; flex: none; fill: var(--brand-red); }
</style>
</head>
<body>

<section class="card card--back" aria-label="Business card back">
  <div class="wordmark">
    <span class="wordmark__main">Mesa Ridge</span>
    <span class="wordmark__sub">Fiberglass</span>
  </div>
</section>

<section class="card card--front" aria-label="Business card front">
  <svg class="card__shapes" viewBox="0 0 620 354" preserveAspectRatio="none" aria-hidden="true">
    <defs>
      <linearGradient id="navyFill" x1="0" y1="1" x2="1" y2="0">
        <stop offset="0" stop-color="#1d2a5e"/>
        <stop offset="1" stop-color="#3a4c85"/>
      </linearGradient>
    </defs>
    <polygon points="0,186 262,226 620,26 620,44 262,232 0,204" fill="var(--brand-red-dark)"/>
    <polygon points="0,178 262,220 620,14 620,30 262,228 0,196" fill="var(--brand-red)"/>
    <polygon points="0,210 262,238 620,50 620,354 0,354" fill="url(#navyFill)"/>
  </svg>

  <div class="wordmark">
    <span class="wordmark__main">Mesa Ridge</span>
    <span class="wordmark__sub">Fiberglass</span>
  </div>

  <div class="person">
    <p class="person__role">Director</p>
    <p class="person__name">Dana Reyes</p>
  </div>

  <div class="divider"></div>

  <ul class="contact">
    <li class="contact__item">
      <svg class="contact__icon" viewBox="0 0 24 24"><path d="M6.6 10.8a15.1 15.1 0 0 0 6.6 6.6l2.2-2.2c.3-.3.7-.4 1-.2 1.1.4 2.3.6 3.6.6.6 0 1 .4 1 1V20c0 .6-.4 1-1 1C10.6 21 3 13.4 3 4c0-.6.4-1 1-1h3.5c.6 0 1 .4 1 1 0 1.3.2 2.5.6 3.6.1.3 0 .7-.2 1z"/></svg>
      <span>1234 5678 90</span>
    </li>
    <li class="contact__item">
      <svg class="contact__icon" viewBox="0 0 24 24"><path d="M2 5h20v14H2z M3.5 6.5l8.5 6.5 8.5-6.5" stroke="var(--navy)" stroke-width="1.6"/></svg>
      <span>info@mesaridgefiberglass.com</span>
    </li>
    <li class="contact__item contact__item--address">
      <svg class="contact__icon" viewBox="0 0 24 24"><path d="M12 2a7 7 0 0 0-7 7c0 5.2 7 13 7 13s7-7.8 7-13a7 7 0 0 0-7-7zm0 9.5A2.5 2.5 0 1 1 12 6.5a2.5 2.5 0 0 1 0 5z"/></svg>
      <span>99 dummy city, dummy place, Dummy Land</span>
    </li>
  </ul>
</section>

</body>
</html>
```